Visitenkarten-Design für Immobilien-Unternehmen
Zielgruppe
Die TORVEL Immobilien GmbH ist eine durch Ing. Gregor Lindqvist inhabergeführte Gesellschaft, welche sich schwerpunktmäßig mit Immobilieninvestitionen sowie Beteiligungen im Bereich von Wohn- und Gewerbeimmobilien beschäftigt. Das Unternehmen kauft, hält, vermietet und verkauft Liegenschaften aller Art, mit dem Fokus auf Gewerbe- und Wohnimmobilien. Zielgruppe sind Personen, welche Immobilien verkaufen möchten - wir betreiben nur eigene Vermögensverwaltung
siehe: www.torvel-immobilien.example
Aufgabenstellung
schlicht und einfach gehalten - weniger ist mehr - nur die wichtigsten Informationen auf der Visitenkarte.
siehe Homepage: www.torvel-immobilien.example

```html
<!DOCTYPE html>
<html lang="de">
<head>
<meta charset="utf-8">
<title>TORVEL Immobilien GmbH – Visitenkarte</title>
<link rel="stylesheet" href="https://fonts.googleapis.com/css2?family=Open+Sans:wght@400;700&display=swap">
<style>
  :root {
    --page-bg: #ffffff;
    --card-dark: #3b3b3c;
    --card-light: #ffffff;
    --frame-line: #9a9a9a;
    --card-edge: #bdbdbd;
    --text-light: #ffffff;
    --text-body: #4a4a4a;
    --text-strong: #3a3a3a;
    --shadow: rgba(0, 0, 0, 0.5);
  }
  * { margin: 0; padding: 0; box-sizing: border-box; }
  html, body {
    width: 1200px;
    height: 1200px;
    overflow: hidden;
    background: var(--page-bg);
    font-family: "Open Sans", Arial, sans-serif;
  }
  .canvas {
    position: relative;
    width: 1200px;
    height: 1200px;
  }
  .card {
    position: absolute;
    top: 438px;
    width: 500px;
    height: 324px;
    box-shadow: 14px 14px 10px var(--shadow);
  }
  .card--front {
    left: 80px;
    background: var(--card-dark);
  }
  .card--front .card__frame {
    position: absolute;
    inset: 11px;
    border: 1px solid var(--frame-line);
  }
  .card__brand {
    position: absolute;
    left: 0;
    right: 0;
    top: 50%;
    transform: translateY(-50%);
    text-align: center;
    color: var(--text-light);
    font-weight: 400;
    font-size: 28px;
    letter-spacing: 1px;
  }
  .card--back {
    left: 620px;
    background: var(--card-light);
    border: 2px solid var(--card-edge);
  }
  .contact {
    position: absolute;
    left: 0;
    right: 0;
    top: 48px;
    text-align: center;
    color: var(--text-body);
    font-size: 18px;
    line-height: 29px;
  }
  .contact__block + .contact__block { margin-top: 29px; }
  .contact__web {
    font-weight: 700;
    color: var(--text-strong);
  }
</style>
</head>
<body>
  <main class="canvas">
    <section class="card card--front" aria-label="Vorderseite">
      <div class="card__frame"></div>
      <p class="card__brand">TORVEL Immobilien GmbH</p>
    </section>

    <section class="card card--back" aria-label="Rückseite">
      <div class="contact">
        <p class="contact__block">
          TORVEL Immobilien GmbH<br>
          Lindenweg 42/3<br>
          AT-8010 Talheim
        </p>
        <p class="contact__block">
          office@torvel-immobilien.example<br>
          +43 660 000 48 21
        </p>
        <p class="contact__block contact__web">www.torvel-immobilien.example</p>
      </div>
    </section>
  </main>
</body>
</html>
```